Law Firm Ad

We need a magazine/auction program design for a Sacramento based law firm. Current need is for a school auction sponsorship. Ad must be 5 1/2 x 8 1/2 in high resolution (300 dpi) and in JPG or PDF format. A clean, modern, simple design is preferred.

Thornby Law Corporation provides general preventative employment advice to employers in avoiding litigation and has counseled businesses on cases involving employment law, unfair business practices and trade secrets. Thornby Law Corporation also practices in business, real estate and employment litigation.

Target Market(s)

This particular ad it is to support Haskeldale Elementary School's 21st Annual Auction and Dinner on March 14, 2015.
Here's the facebook link https://www.examplesocial.test/HaskeldaleAuction/photos/a.918273645012398.275103.610294857361042/3049182736450192/?type=1&theater
But I would like something that might be fairly universal.

Industry/Entity Type

Real Estate

Font styles to use
Sans Serif

Requirements
Must have
• Clean and crisp design. Not overly traditional.
Nice to have
• Contact information:
Thornby Law Corporation
318 Brimley Avenue, Suite 200
Sacramento, CA 95000
916.555.0142
thornby-law.test

```html
<!DOCTYPE html>
<html lang="en">
<head>
<meta charset="utf-8">
<title>Thornby Law Firm Magazine Ad_03</title>
<link rel="stylesheet" href="https://fonts.googleapis.com/css2?family=Arimo:wght@400;700&family=Caladea&display=swap">
<style>
  :root {
    --page-bg: #ffffff;
    --brand-orange: #e0922f;
    --ink: #1f1f1f;
    --muted: #7a7a7a;
    --frame: #cfcfcf;
    --photo-light: #b9b9b9;
    --photo-dark: #6f6f6f;
  }
  * { margin: 0; padding: 0; box-sizing: border-box; }
  html, body {
    width: 1200px; height: 1000px; overflow: hidden;
    background: var(--page-bg);
  }
  .canvas { position: relative; width: 1200px; height: 1000px; }
  .sheet-title {
    position: absolute; top: 64px; left: 0; width: 1200px;
    text-align: center;
    font: 21px/1 "Caladea", Georgia, serif;
    color: var(--ink);
  }
  .ad {
    position: absolute; left: 328px; top: 110px;
    width: 545px; height: 842px;
    background: var(--page-bg);
    border: 1px solid var(--frame);
    box-shadow: 3px 4px 6px rgba(0,0,0,0.28);
    font-family: "Arimo", Helvetica, Arial, sans-serif;
    overflow: hidden;
  }
  .brand-name {
    position: absolute; right: 49px; top: 48px;
    font-size: 20px; font-weight: 700;
    color: var(--brand-orange);
    letter-spacing: -0.2px;
  }
  .hero-photo {
    position: absolute; left: 0; top: 120px;
    width: 545px; height: 363px;
    background: linear-gradient(180deg, var(--photo-dark) 0%, #979797 45%, var(--photo-light) 100%);
  }
  .headline {
    position: absolute; left: 49px; top: 515px;
    font-size: 27.5px; line-height: 36px; font-weight: 400;
    color: var(--brand-orange);
  }
  .contact {
    position: absolute; left: 49px; top: 656px;
    font-size: 12.5px; line-height: 16.5px;
    color: var(--ink); font-style: normal;
  }
  .website {
    position: absolute; left: 49px; top: 739px;
    font-size: 12.5px; font-weight: 700; color: var(--ink);
  }
  .copyright {
    position: absolute; left: 49px; top: 771px;
    font-size: 9.5px; color: var(--muted);
  }
  .footer-band {
    position: absolute; left: 0; bottom: 0;
    width: 545px; height: 24px;
    background: var(--brand-orange);
  }
</style>
</head>
<body>
<div class="canvas">
  <h1 class="sheet-title">Thornby Law Firm Magazine Ad_03</h1>

  <article class="ad">
    <div class="brand-name">Thornby Law Corporation</div>

    <div class="hero-photo" role="img" aria-label="Black-and-white photo of a sprinter wearing bib 110 breaking the finish-line tape against a cloudy sky"></div>

    <h2 class="headline">We are proud to support<br>Haskeldale Elementary School’s<br>21st Annual Auction &amp; Dinner</h2>

    <address class="contact">
      Thornby Law Corporation<br>
      318 Brimley Avenue, Suite 200<br>
      Sacramento, CA 95000<br>
      916.555.0142
    </address>

    <p class="website">thornby-law.test</p>
    <p class="copyright">© 2015 Thornby Law Corporation. All rights reserved.</p>

    <div class="footer-band"></div>
  </article>
</div>
</body>
</html>
```